Special release wine label

Marrow Creek Cellars is a small premium wine producer in the Barossa - South Australia. We are a five star rated winery, producing exceptional wines true to variety, region and house style. We have a very special parcel of wine that we wish to release as an exclusive wine. Visit www.marrowcreekcellars.com.au for further feel.

The wine will be called Marrow Creek Cellars, 2012, The Amber Reserve Shiraz - Cabernet.

The wine can be bottled in either a burgundy or Bordeaux shaped bottle

```html
<!DOCTYPE html>
<html lang="en">
<head>
<meta charset="utf-8">
<title>Marrow Creek Cellars – The Amber Reserve Label</title>
<link href="https://fonts.googleapis.com/css2?family=Cinzel:wght@400;600&family=Oswald:wght@500;600&family=Yellowtail&display=swap" rel="stylesheet">
<style>
  :root {
    --backdrop: #ece6da;
    --paper: #ffffff;
    --paper-shade: #f1f1f1;
    --wine-ink: #5a2430;
    --rule: #b9a3a8;
    --band-red: #c8202f;
    --band-text: #ffffff;
    --band-rule: rgba(255, 255, 255, 0.7);
    --sketch-tone: #e9e2e3;
    --sketch-tone-deep: #d8cccf;
    --small-ink: #6b5a5e;
  }
  html, body {
    margin: 0;
    width: 1200px;
    height: 900px;
    overflow: hidden;
    background: var(--backdrop);
  }
  .canvas {
    position: relative;
    width: 1200px;
    height: 900px;
  }
  .label {
    position: absolute;
    left: 475px;
    top: 20px;
    width: 250px;
    height: 860px;
    overflow: hidden;
    background: linear-gradient(90deg, var(--paper-shade) 0%, var(--paper) 25%, var(--paper) 75%, var(--paper-shade) 100%);
    box-shadow: 0 6px 24px rgba(60, 40, 30, 0.18);
    text-align: center;
    color: var(--wine-ink);
  }
  .winery-name {
    position: absolute;
    top: 42px;
    left: 0;
    right: 0;
    margin: 0;
    font-family: "Cinzel", serif;
    font-weight: 600;
    font-size: 22px;
    line-height: 28px;
    letter-spacing: 1px;
  }
  .winery-rule {
    position: absolute;
    top: 80px;
    left: 34px;
    right: 34px;
    height: 1px;
    background: var(--rule);
  }
  .winery-sub {
    position: absolute;
    top: 90px;
    left: 0;
    right: 0;
    margin: 0;
    font-family: "Cinzel", serif;
    font-weight: 600;
    font-size: 12px;
    line-height: 16px;
    letter-spacing: 3px;
  }
  .homestead-sketch {
    position: absolute;
    top: 160px;
    left: 30px;
    width: 190px;
    height: 150px;
    background: radial-gradient(ellipse at 50% 60%, var(--sketch-tone-deep) 0%, var(--sketch-tone) 55%, var(--paper) 100%);
  }
  .release-band {
    position: absolute;
    top: 398px;
    left: 0;
    width: 250px;
    height: 245px;
  }
  .release-band svg {
    position: absolute;
    inset: 0;
  }
  .release-name {
    position: absolute;
    top: 22px;
    left: 0;
    right: 0;
    margin: 0;
    font-family: "Yellowtail", cursive;
    font-size: 21px;
    line-height: 28px;
    color: var(--band-text);
  }
  .release-rule {
    position: absolute;
    top: 56px;
    left: 34px;
    right: 34px;
    height: 1px;
    background: var(--band-rule);
  }
  .variety {
    position: absolute;
    top: 68px;
    left: 0;
    right: 0;
    margin: 0;
    font-family: "Oswald", sans-serif;
    font-weight: 600;
    color: var(--band-text);
    line-height: 1;
    text-transform: uppercase;
  }
  .variety .line-one { display: block; font-size: 46px; }
  .variety .line-two { display: block; font-size: 37px; margin-top: 6px; }
  .vintage {
    position: absolute;
    top: 178px;
    left: 0;
    right: 0;
    display: flex;
    align-items: center;
    justify-content: center;
    gap: 12px;
    font-family: "Yellowtail", cursive;
    font-size: 18px;
    line-height: 24px;
    color: var(--band-text);
  }
  .vintage::before,
  .vintage::after {
    content: "";
    width: 28px;
    height: 1px;
    background: var(--band-rule);
  }
  .volume {
    position: absolute;
    top: 708px;
    left: 0;
    right: 0;
    margin: 0;
    font-family: "Cinzel", serif;
    font-weight: 600;
    font-size: 15px;
    line-height: 20px;
    letter-spacing: 1.5px;
  }
  .region {
    position: absolute;
    top: 828px;
    left: 0;
    right: 0;
    margin: 0;
    font-family: "Cinzel", serif;
    font-size: 9px;
    line-height: 12px;
    letter-spacing: 2px;
    color: var(--small-ink);
  }
</style>
</head>
<body>
<main class="canvas">
  <section class="label">
    <h1 class="winery-name">Marrow Creek</h1>
    <div class="winery-rule"></div>
    <p class="winery-sub">Cellars</p>

    <div class="homestead-sketch" role="img" aria-label="Ink sketch of the cellar homestead framed by tall palm trees"></div>

    <div class="release-band">
      <svg width="250" height="245" viewBox="0 0 250 245" aria-hidden="true">
        <path d="M0 4 L60 0 L140 3 L250 0 L250 232 L215 228 L180 236 L140 230 L100 238 L60 231 L25 237 L0 233 Z" fill="var(--band-red)"/>
      </svg>
      <p class="release-name">The Amber Reserve</p>
      <div class="release-rule"></div>
      <h2 class="variety"><span class="line-one">Shiraz</span><span class="line-two">Cabernet</span></h2>
      <div class="vintage">2012</div>
    </div>

    <p class="volume">750 ML</p>
    <p class="region">South Australia</p>
  </section>
</main>
</body>
</html>
```